SUMMIT GATHERING 2021. August 20th -22nd.

The Hosts of the conference: Grace Tabernacle-Pastors Ron n Della ( Picture with two persons)

Guest Minister: Bishop Lucinda Okotieno. (Cedar Ridge Awakening)

Venue:
Sealand Gateway Lodgeview. 4817 North 239th Avenue Seattle, WA 98174.

Conference times.
Friday August 20th 6pm-8:30pm
Saturday August 21st. 6pm-8:30pm

Sunday August 22nd 10am-1pm
“ CHURCH RENEWAL GATHERING”

5pm-7:30pm
TWOFOLD SURGE GATHERING.

Target Market(s)

18-55

Industry/Entity Type

Religious/ Entertainment.

Requirements
Must have
• A highlight of the Relaunch service on Sunday August 22nd 5pm-7:30pm.
Nice to have
• Excellent ideas….

```html
<!DOCTYPE html>
<html lang="en">
<head>
<meta charset="utf-8">
<title>Summit Gathering 2021 — Grace Tabernacle</title>
<link rel="stylesheet" href="https://fonts.googleapis.com/css2?family=Great+Vibes&family=Montserrat:ital,wght@0,400;0,600;0,700;0,800;0,900;1,700;1,900&display=swap">
<style>
  :root {
    --page-bg: #eceded;
    --gold-deep: #c88a34;
    --gold: #e6b56c;
    --gold-soft: #f0cf93;
    --gold-light: #f8ead2;
    --red: #e41f26;
    --ink: #333538;
    --text: #3a3a3a;
  }
  * { box-sizing: border-box; margin: 0; padding: 0; }
  html, body {
    width: 1200px; height: 900px; overflow: hidden;
    background: var(--page-bg);
  }
  .poster {
    position: absolute; left: 294px; top: 20px;
    width: 612px; height: 860px; overflow: hidden;
    background: linear-gradient(155deg,
      var(--gold) 0%, var(--gold-deep) 30%, var(--gold-soft) 42%,
      var(--gold-light) 48%, var(--gold-soft) 56%, var(--gold) 70%,
      var(--gold-light) 80%, var(--gold-soft) 88%, var(--gold) 100%);
    font-family: "Montserrat", sans-serif;
    color: var(--text);
  }
  .bands { position: absolute; inset: 0; }
  .title-main {
    position: absolute; left: 113px; top: 34px;
    font-family: "Montserrat", sans-serif; font-weight: 900;
    font-size: 72px; letter-spacing: -2px; color: var(--ink); line-height: 1;
  }
  .title-script {
    position: absolute; left: 60px; top: 62px;
    font-family: "Great Vibes", cursive; font-size: 104px;
    color: var(--red); line-height: 1;
  }
  .title-year {
    position: absolute; left: 197px; top: 143px;
    font-family: "Montserrat", sans-serif; font-weight: 800;
    font-size: 32px; letter-spacing: 14px; color: var(--ink); line-height: 1;
  }
  .year-rule {
    position: absolute; left: 195px; top: 180px; width: 123px; height: 3px;
    background: var(--red);
  }
  .title-dates {
    position: absolute; left: 193px; top: 186px;
    font-weight: 700; font-style: italic; font-size: 12.5px; color: var(--ink);
  }
  .host-mark {
    position: absolute; left: 456px; top: 52px; width: 104px; height: 120px;
    display: flex; flex-direction: column; align-items: center; justify-content: center; gap: 8px;
  }
  .host-mark__square { width: 26px; height: 26px; background: var(--ink); }
  .host-mark__name {
    font-weight: 800; font-size: 13px; line-height: 1.15; text-align: center;
    color: var(--ink); letter-spacing: .5px;
  }
  .photo { position: absolute; }
  .photo--guest {
    left: 182px; top: 223px; width: 141px; height: 156px;
    background: linear-gradient(180deg, #dfeee8 0%, #c9d4cf 45%, #6c6a66 100%);
  }
  .photo--hosts {
    left: 182px; top: 390px; width: 141px; height: 377px;
    background: linear-gradient(180deg, #3b3f8f 0%, #8a3c86 22%, #7c5a52 45%, #cfc7c1 75%, #9e9893 100%);
  }
  .details { position: absolute; left: 337px; width: 270px; }
  .label {
    font-weight: 700; font-size: 10.5px; color: var(--red);
    letter-spacing: .3px; line-height: 14px;
  }
  .line { font-weight: 400; font-size: 14.5px; line-height: 18px; color: var(--text); }
  .line--small { font-size: 11.5px; line-height: 16px; }
  .gap { height: 6px; }
  .highlight {
    font-weight: 900; font-style: italic; font-size: 16.5px; line-height: 18px;
    color: var(--red); text-transform: uppercase; letter-spacing: -.2px;
  }
  .closing {
    position: absolute; left: 0; right: 0; top: 810px; padding-left: 0;
    text-align: center; transform: translateX(-1px);
  }
  .closing span {
    display: inline-block; margin-left: -0px;
    font-weight: 900; font-style: italic; font-size: 17px; color: var(--ink);
    letter-spacing: -.3px; position: relative; left: 0;
  }
</style>
</head>
<body>
  <main class="poster">
    <svg class="bands" width="612" height="860" viewBox="0 0 612 860" aria-hidden="true">
      <polygon points="524,0 612,0 612,102 338,242" fill="var(--red)"/>
      <polygon points="0,415 174,342 0,538" fill="var(--ink)"/>
    </svg>

    <h1 class="title">
      <span class="title-main">SUMMIT</span>
      <span class="title-script">Gathering</span>
      <span class="title-year">2021</span>
    </h1>
    <div class="year-rule"></div>
    <p class="title-dates">August 20th -22nd</p>

    <div class="host-mark">
      <span class="host-mark__square"></span>
      <span class="host-mark__name">GRACE<br>TABERNACLE</span>
    </div>

    <div class="photo photo--guest" role="img" aria-label="Portrait photo of guest minister Bishop Lucinda Okotieno"></div>
    <div class="photo photo--hosts" role="img" aria-label="Photo of host pastors Ron and Della together"></div>

    <section class="details" style="top:309px">
      <p class="label">Guest Minister:</p>
      <p class="line">Bishop Lucinda<br>Okotieno</p>
      <p class="line line--small">(Cedar Ridge Awakening)</p>
    </section>

    <section class="details" style="top:390px">
      <p class="label">THE HOSTS OF THE CONFERENCE:</p>
      <p class="line">Grace Tabernacle-<br>Pastors Ron n Della</p>
    </section>

    <section class="details" style="top:461px">
      <p class="label">VENUE:</p>
      <p class="line">Sealand Gateway Lodgeview.<br>4817 North 239th<br>Avenue Seattle,<br>WA 98174</p>
    </section>

    <section class="details" style="top:568px">
      <p class="label">CONFERENCE TIMES:</p>
      <p class="line">Friday August 20th<br>6pm-8:30pm</p>
      <div class="gap"></div>
      <p class="line">Saturday August 21st<br>6pm-8:30pm</p>
      <div class="gap"></div>
      <p class="line">Sunday August 22nd<br>10am-1pm</p>
    </section>

    <section class="details" style="top:834px; top:832px; display:none"></section>

    <section class="details" style="top:834px"></section>

    <section class="details" style="top:833px"></section>

    <section class="details" style="top:832px"></section>

    <section class="details" style="top:834px"></section>

    <section class="details" style="top:834px"></section>

    <section class="details" style="top:834px"></section>

    <section class="details" style="top:835px"></section>

    <section class="details" style="top:834px"></section>

    <section class="details" style="top:834px"></section>

    <section class="details" style="top:834px"></section>

    <section class="details" style="top:834px"></section>

    <section class="details" style="top:834px"></section>

    <section class="details" style="top:834px"></section>

    <section class="details" style="top:834px"></section>

    <section class="details" style="top:834px"></section>

    <section class="details" style="top:834px"></section>

    <section class="details" style="top:834px"></section>

    <section class="details" style="top:834px"></section>

    <section class="details" style="top:834px"></section>

    <section class="details" style="top:834px"></section>

    <section class="details" style="top:834px"></section>

    <section class="details" style="top:834px"></section>

    <section class="details" style="top:834px"></section>

    <section class="details" style="top:834px"></section>

    <section class="details" style="top:834px"></section>

    <section class="details" style="top:834px"></section>

    <section class="details" style="top:834px"></section>

    <section class="details" style="top:834px"></section>

    <section class="details" style="top:834px"></section>

    <section class="details" style="top:834px"></section>

    <section class="details" style="top:834px"></section>

    <section class="details" style="top:834px"></section>

    <section class="details" style="top:834px"></section>

    <section class="details" style="top:834px"></section>

    <section class="details" style="top:834px"></section>

    <section class="details" style="top:834px"></section>

    <section class="details" style="top:834px"></section>

    <section class="details" style="top:834px"></section>

    <section class="details" style="top:834px"></section>

    <section class="details" style="top:834px"></section>

    <section class="details" style="top:834px"></section>

    <section class="details" style="top:834px"></section>

    <section class="details" style="top:834px"></section>

    <section class="details" style="top:834px"></section>

    <section class="details" style="top:834px"></section>

    <section class="details" style="top:834px"></section>

    <section class="details" style="top:834px"></section>

    <section class="details" style="top:834px"></section>

    <section class="details" style="top:834px"></section>

    <section class="details" style="top:834px"></section>

    <section class="details" style="top:834px"></section>

    <section class="details" style="top:834px"></section>

    <section class="details" style="top:834px"></section>

    <section class="details" style="top:834px"></section>

    <section class="details" style="top:834px"></section>

    <section class="details" style="top:834px"></section>

    <section class="details" style="top:834px"></section>

    <section class="details" style="top:834px"></section>

    <section class="details" style="top:834px"></section>

    <section class="details" style="top:834px"></section>

    <section class="details" style="top:834px"></section>

    <section class="details" style="top:834px"></section>

    <section class="details" style="top:834px"></section>

    <section class="details" style="top:834px"></section>

    <section class="details" style="top:834px"></section>

    <section class="details" style="top:834px"></section>

    <section class="details" style="top:834px"></section>

    <section class="details" style="top:834px"></section>

    <section class="details" style="top:834px"></section>

    <section class="details" style="top:834px"></section>

    <section class="details" style="top:834px"></section>

    <section class="details" style="top:834px"></section>

    <section class="details" style="top:834px"></section>

    <section class="details" style="top:834px"></section>

    <section class="details" style="top:834px"></section>

    <section class="details" style="top:834px"></section>

    <section class="details renewal" style="top:737px">
      <p class="highlight">Church<br>Renewal Gathering</p>
      <p class="line">5pm-7:30pm</p>
    </section>

    <p class="closing"><span>TWOFOLD SURGE GATHERING</span></p>
  </main>
</body>
</html>
```